needing web design for aerial and satellite installation comapny

We need our website designing, it needs to be professional and look creative,
We are a aerial and satellite company called Brindle Fixing & Tending ()
I like this site design also some of the following maybe:

https://www.corvimast.co.uk/

http://quellmoor.co.uk/

http://larkpin4guard.co.uk/portfolio/tdn-quellmoor/

The design will require coding once the design is complete, i haven't paid for this yet as i want to be sure the design is good before i commit.

The template needs to look professional and look like one of the leading companies.
The site will consist of all the features this site has https://www.corvimast.co.uk/

I like a modern design with the latest technology.

Target Market(s)

tv aerial satellite installation

Industry/Entity Type

Satellite Tv

Number of Pages Required

3 page

Font styles to use
Sans Serif

Colors

Designer to choose colors to be used in the design.

Requirements
Must have
• eb Contest Brief We need our website designing, it needs to be professional and look creative,
• We are a aerial and satellite company called Brindle Fixing Tending ()
• I like this site design also some of the following maybe:
• https://www.corvimast.co.uk/
• http://quellmoor.co.uk/
• http://larkpin4guard.co.uk/portfolio/tdn-quellmoor/
• The design will require coding once the design is complete, i haven't paid for this yet as i want to be sure the design is good before i commit.
• The template needs to look professional and look like one of the leading companies.
• The site will consist of all the features this site has https://www.corvimast.co.uk/
• I like a modern design with the latest technology.
Nice to have
• http://quellmoor.co.uk/
Should not have
• poor design

```html
<!DOCTYPE html>
<html lang="en">
<head>
<meta charset="utf-8">
<title>Brindle Fixing &amp; Tending — Why Us</title>
<link rel="stylesheet" href="https://fonts.googleapis.com/css2?family=Raleway:wght@300;400;500&family=Oswald:wght@500&family=Open+Sans:wght@600&display=swap">
<style>
  :root {
    --bg-top: #f7f7f8;
    --bg-why: #ececec;
    --orange: #e8900f;
    --navy: #1c2436;
    --navy-panel: #14213a;
    --text: #454545;
    --rule: #8a8a8a;
    --icon-grey: #4a4a4a;
    --white: #ffffff;
  }
  * { box-sizing: border-box; margin: 0; padding: 0; }
  html, body { width: 1200px; height: 1200px; overflow: hidden; }
  body { position: relative; font-family: "Raleway", sans-serif; color: var(--text); background: var(--bg-why); }

  .intro { position: absolute; left: 0; top: 0; width: 1200px; height: 157px; background: var(--bg-top); }
  .btn-about {
    position: absolute; left: 519px; top: 58px; width: 162px; height: 33px;
    background: var(--orange); color: var(--white);
    font: 600 11px/33px "Open Sans", sans-serif; text-align: center; letter-spacing: .3px;
  }

  .why { position: absolute; left: 0; top: 157px; width: 1200px; height: 611px; background: var(--bg-why); }
  .why-kicker { position: absolute; top: 30px; width: 100%; text-align: center; font: 300 30px/1 "Raleway", sans-serif; color: var(--orange); letter-spacing: 1px; }
  .why-title { position: absolute; top: 70px; width: 100%; text-align: center; font: 400 31px/1 "Raleway", sans-serif; color: var(--navy); letter-spacing: 1.5px; }
  .rule-v { position: absolute; left: 600px; top: 125px; width: 1px; height: 424px; background: var(--rule); }
  .rule-h { position: absolute; left: 120px; top: 326px; width: 960px; height: 1px; background: var(--rule); }

  .feature-icon { position: absolute; }
  .feature-title { position: absolute; font: 400 15.5px/1 "Raleway", sans-serif; color: var(--navy); letter-spacing: .6px; }
  .feature-text { position: absolute; font: 400 12px/19.2px "Raleway", sans-serif; color: var(--text); letter-spacing: .3px; }

  .sectors { position: absolute; left: 0; top: 768px; width: 596px; height: 432px; background: var(--navy-panel); }
  .sectors-title { position: absolute; left: 207px; top: 38px; font: 500 20px/1 "Oswald", sans-serif; color: var(--white); letter-spacing: 1px; }
  .sector { position: absolute; left: 0; width: 596px; height: 50px; }
  .sector-icon { position: absolute; left: 202px; top: 0; }
  .sector-label { position: absolute; left: 282px; top: 0; font: 500 15px/50px "Raleway", sans-serif; color: var(--white); letter-spacing: .8px; white-space: nowrap; }
  .sector.is-active .sector-label { color: var(--orange); }
  .pointer { position: absolute; left: 456px; top: 226px; }

  .dish-photo { position: absolute; left: 596px; top: 768px; width: 604px; height: 432px;
    background: linear-gradient(160deg, #8ea8d4 0%, #5576b0 45%, #2d4f8e 100%); }
</style>
</head>
<body>

<section class="intro">
  <div class="btn-about">ABOUT US</div>
</section>

<section class="why">
  <div class="why-kicker">Why</div>
  <h2 class="why-title">Brindle Fixing Tending</h2>
  <div class="rule-v"></div>
  <div class="rule-h"></div>

  <!-- Trust & Reliability -->
  <svg class="feature-icon" style="left:120px;top:143px" width="66" height="66" viewBox="0 0 66 66">
    <circle cx="25" cy="40" r="17" fill="none" stroke="var(--icon-grey)" stroke-width="6" stroke-dasharray="5 4"/>
    <circle cx="25" cy="40" r="13" fill="var(--bg-why)" stroke="var(--icon-grey)" stroke-width="1.5"/>
    <path d="M31 40a6 6 0 1 1-3-5" fill="none" stroke="var(--icon-grey)" stroke-width="1.5"/>
    <circle cx="46" cy="19" r="13" fill="none" stroke="var(--orange)" stroke-width="6" stroke-dasharray="4 3"/>
    <circle cx="46" cy="19" r="10" fill="var(--orange)"/>
    <circle cx="46" cy="19" r="4" fill="var(--bg-why)"/>
  </svg>
  <h3 class="feature-title" style="left:214px;top:169px">Trust &amp; Reliability</h3>
  <p class="feature-text" style="left:214px;top:195px;width:345px">We only use quality components and fixings. Our engineers are fully trained and up to date with the technologies of today. As a company we are fully insured, and follow all industry standards and procedures.</p>

  <!-- Our Services -->
  <svg class="feature-icon" style="left:634px;top:153px" width="60" height="70" viewBox="0 0 60 70">
    <rect x="0" y="0" width="46" height="68" fill="var(--icon-grey)"/>
    <g fill="var(--white)">
      <rect x="12" y="10" width="18" height="2.5"/>
      <rect x="8" y="20" width="2.5" height="2.5"/><rect x="13" y="20" width="22" height="2.5"/>
      <rect x="8" y="28" width="2.5" height="2.5"/><rect x="13" y="28" width="22" height="2.5"/>
      <rect x="8" y="36" width="2.5" height="2.5"/><rect x="13" y="36" width="16" height="2.5"/>
      <rect x="8" y="44" width="2.5" height="2.5"/><rect x="13" y="44" width="12" height="2.5"/>
      <rect x="8" y="52" width="2.5" height="2.5"/><rect x="13" y="52" width="12" height="2.5"/>
    </g>
    <circle cx="41" cy="44" r="17" fill="var(--bg-why)"/>
    <circle cx="41" cy="44" r="14" fill="var(--orange)"/>
    <path d="M34 44l5 5 9-10" fill="none" stroke="var(--white)" stroke-width="3.5" stroke-linecap="round" stroke-linejoin="round"/>
  </svg>
  <h3 class="feature-title" style="left:722px;top:154px">Our Services</h3>
  <p class="feature-text" style="left:725px;top:177px;width:340px">We are specialists in Smart Home TV Aerial &amp; Satellite Installations, and offer the Same Day Response for our services.Brindle Fixing &amp; Tending are recognised by our industry for having a reputation for trust, reliability, quality of work, and best all round value.</p>

  <!-- Our Coverage -->
  <svg class="feature-icon" style="left:120px;top:390px" width="64" height="72" viewBox="0 0 64 72">
    <polygon points="32,0 64,17 32,34 0,17" fill="var(--icon-grey)"/>
    <polygon points="40,4 56,13 26,29 10,21" fill="var(--orange)"/>
    <polygon points="0,20 30,37 30,72 0,55" fill="var(--icon-grey)"/>
    <polygon points="34,37 64,20 64,55 34,72" fill="var(--icon-grey)"/>
    <polygon points="12,30 18,33 18,55 12,52" fill="var(--bg-why)"/>
  </svg>
  <h3 class="feature-title" style="left:218px;top:412px">Our Coverage</h3>
  <p class="feature-text" style="left:219px;top:434px;width:330px">We can in most cases provide the Same Day Call Out Services for Aerial &amp; Satellite Installations, including Skylark Satellite TV, Openbeam, and Clearair, and supporting products and services.</p>

  <!-- Same Day -->
  <svg class="feature-icon" style="left:632px;top:381px" width="68" height="68" viewBox="0 0 68 68">
    <path d="M0 0H46V50L24 56L0 68Z" fill="var(--icon-grey)"/>
    <path d="M0 0H46V38L24 56L0 68Z" fill="var(--icon-grey)"/>
    <circle cx="46" cy="34" r="20" fill="var(--bg-why)"/>
    <circle cx="46" cy="34" r="17" fill="var(--white)" stroke="var(--icon-grey)" stroke-width="2.5"/>
    <path d="M46 25v18M37 34h18" stroke="var(--orange)" stroke-width="5"/>
  </svg>
  <h3 class="feature-title" style="left:724px;top:400px">Same Day TV Aerial Installations</h3>
  <p class="feature-text" style="left:722px;top:428px;width:350px">Our coverage allows us to offer the Same Day Service for both TV Aerial Installations and Repairs. Or within 24 Hours of contact.All our TV Aerial Engineers are well trained, and being locally based, are very familiar with the areas that we cover.</p>
</section>

<section class="sectors">
  <h2 class="sectors-title">Sector coverage</h2>

  <div class="sector" style="top:130px">
    <svg class="sector-icon" width="60" height="44" viewBox="0 0 60 44" style="top:3px">
      <g stroke="var(--white)" stroke-width="1.3" fill="none">
        <path d="M1 8L52 24"/>
        <path d="M10 8v5M16 10v5M22 12v5M28 14v5M34 16v5M40 18v5"/>
        <path d="M52 6L44 40M58 10L50 44M52 24l6-14"/>
        <path d="M46 30h10M47 26h10M48 22h8"/>
      </g>
    </svg>
    <div class="sector-label">TV Aerial Services</div>
  </div>

  <div class="sector is-active" style="top:187px">
    <svg class="sector-icon" width="60" height="44" viewBox="0 0 60 44" style="top:3px">
      <ellipse cx="32" cy="19" rx="13" ry="18" transform="rotate(20 32 19)" fill="var(--orange)"/>
      <path d="M24 30l-12 8M10 35l5 6" stroke="var(--orange)" stroke-width="3" fill="none"/>
      <circle cx="31" cy="14" r="1" fill="var(--navy-panel)"/><circle cx="35" cy="22" r="1" fill="var(--navy-panel)"/>
    </svg>
    <div class="sector-label">Skylark Satellite TV Services</div>
    <svg class="pointer" width="18" height="18" viewBox="0 0 18 18" style="top:32px;left:456px">
      <path d="M1 1L16 9 10 10 14 16 11 17 7 11 3 15Z" fill="var(--white)"/>
    </svg>
  </div>

  <div class="sector" style="top:243px">
    <div class="sector-icon" role="img" aria-label="Two figures holding smart home devices" style="top:-2px;width:58px;height:48px;background:#2a3853"></div>
    <div class="sector-label">Smart Home Systems</div>
  </div>

  <div class="sector" style="top:299px">
    <svg class="sector-icon" width="60" height="44" viewBox="0 0 60 44" style="top:2px">
      <g stroke="var(--white)" stroke-width="1.5" fill="none">
        <rect x="1" y="24" width="16" height="17"/><rect x="21" y="14" width="18" height="27"/><rect x="42" y="24" width="17" height="17"/>
        <path d="M1 32h16M9 24v17M21 22h18M21 31h18M30 14v27M42 32h17M50 24v17"/>
        <path d="M24 14v-8M24 6l-3-3M34 14v-6h4"/>
      </g>
    </svg>
    <div class="sector-label">Communal &amp; Commercial</div>
  </div>

  <div class="sector" style="top:357px">
    <svg class="sector-icon" width="60" height="44" viewBox="0 0 60 44" style="top:2px">
      <g fill="none" stroke="var(--white)" stroke-width="2">
        <rect x="1" y="2" width="8" height="34"/><rect x="51" y="2" width="8" height="34"/>
        <rect x="15" y="6" width="30" height="20"/><path d="M30 26v5M20 33h20"/>
        <path d="M13 38h34"/>
      </g>
      <g fill="var(--white)">
        <circle cx="5" cy="12" r="2"/><circle cx="5" cy="25" r="2.5"/>
        <circle cx="55" cy="12" r="2"/><circle cx="55" cy="25" r="2.5"/>
        <rect x="2" y="37" width="2" height="5"/><rect x="56" y="37" width="2" height="5"/>
      </g>
    </svg>
    <div class="sector-label">Sound &amp; Video Services</div>
  </div>
</section>

<div class="dish-photo" role="img" aria-label="Large white satellite dish against a blue sky"></div>

</body>
</html>
```